ORM/DELK JV

We need a business card design for a joint venture construction company. We have two logos that need to appear and need to be cleaned up. We are looking for a simple design with a white background and black lettering. The company name is R. Malverti, Inc./D. Ellory Construction Corp. J.V.

The website is www.ormdelk.com

Please indicate spaces for phone; fax and cell. For this mockup use the following info:

Gus Perrin
Project Enginner
2871 Route 4
Brookvale, NY 12058
gusormdelk@mailbrook.com
Office: 518-964-31158
Fax: 518-964-8817
Cell: 845-271-6043

Please note; the logos themselves should not include the company names but the card should include the name of the company - R. Malverti, Inc./D. Ellory Construction Corp., J.V. 

Also, the logo should appear alphabetically ORM first, then DELK, but they should be the same size.

Industry/Entity Type

Construction

Requirements
Should not have
• The logos should not include the company name; please crop that from the image.

```html
<!DOCTYPE html>
<html lang="en">
<head>
<meta charset="utf-8">
<title>ORM/DELK JV — Business Card</title>
<link rel="stylesheet" href="https://fonts.googleapis.com/css2?family=Mulish:ital,wght@0,400;0,700;0,800;1,400&display=swap">
<style>
  :root {
    --navy: #2b2a72;
    --red: #a5191e;
    --white: #ffffff;
    --ink: #1b1b1b;
    --backdrop: #d9d9d9;
  }
  * { margin: 0; padding: 0; box-sizing: border-box; }
  html, body {
    width: 1200px;
    height: 1167px;
    overflow: hidden;
    background: var(--backdrop);
    font-family: "Mulish", Arial, sans-serif;
  }
  .card {
    position: absolute;
    left: 100px;
    top: 298px;
    width: 1000px;
    height: 571px;
    overflow: hidden;
    background: var(--navy);
    box-shadow: 0 6px 18px rgba(0,0,0,0.25);
  }
  .card-shape { position: absolute; inset: 0; }
  .brand {
    position: absolute;
    top: 74px;
    font-weight: 800;
    font-size: 58px;
    line-height: 1;
    letter-spacing: 1px;
  }
  .brand--orm { left: 40px; color: var(--red); }
  .brand--delk {
    left: 300px;
    color: var(--navy);
    display: flex;
    align-items: center;
    gap: 14px;
  }
  .brand-square {
    width: 50px;
    height: 50px;
    background: var(--navy);
  }
  .person {
    position: absolute;
    left: 600px;
    top: 36px;
  }
  .person-name {
    font-weight: 800;
    font-size: 28px;
    color: var(--ink);
    letter-spacing: 0.5px;
  }
  .person-title {
    font-style: italic;
    font-size: 18px;
    color: var(--ink);
    margin-top: 2px;
    letter-spacing: 0.5px;
  }
  .company {
    position: absolute;
    left: 30px;
    top: 160px;
    font-weight: 800;
    font-size: 30px;
    line-height: 42px;
  }
  .company-first { color: var(--red); }
  .company-second { color: var(--navy); }
  .contact {
    position: absolute;
    left: 30px;
    top: 250px;
    list-style: none;
    font-size: 24px;
    line-height: 34px;
    color: var(--ink);
    letter-spacing: 0.6px;
  }
  .website {
    position: absolute;
    right: 42px;
    top: 510px;
    font-weight: 700;
    font-size: 30px;
    line-height: 38px;
    color: var(--white);
    letter-spacing: 1px;
  }
</style>
</head>
<body>
  <div class="card">
    <svg class="card-shape" width="1000" height="571" viewBox="0 0 1000 571" aria-hidden="true">
      <rect width="1000" height="571" fill="var(--navy)"/>
      <ellipse cx="330" cy="205" rx="640" ry="330" fill="var(--red)"/>
      <ellipse cx="330" cy="201" rx="624" ry="316" fill="var(--white)"/>
    </svg>

    <div class="brand brand--orm">ORM</div>
    <div class="brand brand--delk"><span class="brand-square"></span>DELK</div>

    <div class="person">
      <div class="person-name">Gus Perrin</div>
      <div class="person-title">Project Enginner</div>
    </div>

    <div class="company">
      <div class="company-first">R. Malverti, Inc./</div>
      <div class="company-second">D. Ellory Construction Corp. J.V.</div>
    </div>

    <ul class="contact">
      <li>2871 Route 4</li>
      <li>Brookvale, NY 12058</li>
      <li>gusormdelk@mailbrook.com</li>
      <li>Office: 518-964-31158</li>
      <li>Fax: 518-964-8817</li>
      <li>Cell: 845-271-6043</li>
    </ul>

    <div class="website">www.ormdelk.com</div>
  </div>
</body>
</html>
```